VORK.
BRIDGING HORIZONS
VORK. -
Creative Brief
Use specific fonts
any thing which suits with the LOGO provided
Professional
RAJESH MOTLA
MR.
B.P. No.6213, COMMUNE-3, NEAR TORAVI LAUNDRY, KALEBA ZONE, BAMAKO-MALI
rajesh@vork.co.in
vork.co.in
pls mention MANAGING DIRECTOR, the designation, below the name of the person.
LOGO at centre. Below mentioned address at bottom: India Office D-47, Palm Enclave-II, Gurgaon, Haryana 122015 ph:+91-124-4708352, fax:+91-124-4519267 cell:+91-9871436029

```html
<!DOCTYPE html>
<html lang="en">
<head>
<meta charset="utf-8">
<title>VORK. Business Card Options</title>
<link href="https://fonts.googleapis.com/css2?family=Open+Sans:ital,wght@0,400;0,600;0,800;1,400;1,600&family=Michroma&display=swap" rel="stylesheet">
<style>
  :root {
    --board: #3b3b3c;
    --card: #ffffff;
    --brand-blue: #1c5fa9;
    --navy: #1f3d78;
    --ink: #4a4f5a;
    --green: #7cb829;
    --green-light: #b5dc4c;
    --blue-light: #3d8fd6;
    --label: #d9d9d9;
  }
  * { box-sizing: border-box; margin: 0; padding: 0; }
  html, body { width: 1200px; height: 809px; overflow: hidden; background: var(--board); }
  body { position: relative; font-family: "Open Sans", Arial, sans-serif; }

  .card {
    position: absolute;
    width: 540px;
    height: 336px;
    background: var(--card);
    border-radius: 16px;
    overflow: hidden;
    box-shadow: 0 2px 6px rgba(0,0,0,.35);
  }
  .front-a { left: 31px;  top: 36px; }
  .front-b { left: 631px; top: 36px; }
  .back-a  { left: 31px;  top: 432px; }
  .back-b  { left: 631px; top: 432px; }

  .option-label {
    position: absolute;
    width: 540px;
    text-align: center;
    font-family: "Michroma", Arial, sans-serif;
    font-size: 13px;
    letter-spacing: 2px;
    color: var(--label);
    font-variant: small-caps;
  }
  .label-front-a { left: 31px;  top: 396px; }
  .label-front-b { left: 631px; top: 396px; }
  .label-back-a  { left: 31px;  top: 786px; }
  .label-back-b  { left: 631px; top: 786px; }

  .brand { position: absolute; display: flex; flex-direction: column; align-items: center; }
  .brand-row { display: flex; align-items: center; gap: 12px; }
  .brand-dot { border-radius: 50%; background: var(--brand-blue); }
  .brand-name {
    font-weight: 800;
    color: var(--brand-blue);
    letter-spacing: 2px;
    line-height: 1;
  }
  .brand-tagline {
    font-weight: 800;
    color: var(--brand-blue);
    letter-spacing: 2px;
    margin-top: 4px;
  }

  .front-a .brand { left: 120px; top: 50px; }
  .front-a .brand-dot { width: 54px; height: 54px; }
  .front-a .brand-name { font-size: 46px; }
  .front-a .brand-tagline { font-size: 11px; }

  .front-b .brand { left: 30px; top: 95px; }
  .front-b .brand-dot { width: 64px; height: 64px; }
  .front-b .brand-name { font-size: 60px; }
  .front-b .brand-tagline { font-size: 13px; }

  .back-a .brand { left: 0; width: 540px; top: 55px; }
  .back-a .brand-dot { width: 70px; height: 70px; }
  .back-a .brand-name { font-size: 60px; }
  .back-a .brand-tagline { font-size: 13px; }

  .back-b .brand { left: 0; width: 540px; top: 70px; }
  .back-b .brand-dot { width: 70px; height: 70px; }
  .back-b .brand-name { font-size: 54px; }

  .contact { position: absolute; color: var(--ink); font-size: 9.5px; line-height: 1.35; }
  .front-a .contact { left: 360px; top: 104px; width: 165px; }
  .front-b .contact { left: 350px; top: 24px; width: 175px; }
  .person-name { font-size: 13px; font-weight: 600; color: var(--navy); }
  .person-title { font-style: italic; margin-bottom: 6px; }
  .address { font-style: italic; margin-bottom: 6px; }
  .contact-row { display: flex; align-items: center; gap: 5px; margin-bottom: 2px; }
  .contact-row svg { width: 9px; height: 9px; flex: none; }
  .front-a .person-name, .front-a .person-title, .front-a .address { text-align: right; }

  .office { position: absolute; left: 0; width: 540px; top: 178px; text-align: center; color: var(--navy); }
  .office-title { font-style: italic; font-size: 16px; font-weight: 600; color: var(--brand-blue); }
  .office-address { font-size: 12px; margin-top: 2px; display: flex; justify-content: center; align-items: center; gap: 5px; }
  .office-phones { font-size: 11.5px; margin-top: 4px; display: flex; justify-content: center; gap: 12px; }
  .office-phones span, .office-address span { display: inline-flex; align-items: center; gap: 4px; }
  .office svg { width: 10px; height: 10px; }

  .swoosh { position: absolute; left: 0; bottom: 0; width: 540px; height: 336px; }
</style>
</head>
<body>

  <!-- Front option A -->
  <section class="card front-a">
    <svg class="swoosh" viewBox="0 0 540 336" aria-hidden="true">
      <defs>
        <linearGradient id="greenA" x1="0" x2="1"><stop offset="0" stop-color="var(--green-light)"/><stop offset="1" stop-color="var(--green)"/></linearGradient>
        <linearGradient id="blueA" x1="0" x2="1"><stop offset="0" stop-color="var(--brand-blue)"/><stop offset="1" stop-color="var(--blue-light)"/></linearGradient>
      </defs>
      <path d="M0,236 C120,284 300,312 540,306 L540,336 L0,336 Z" fill="url(#greenA)"/>
      <path d="M0,264 C140,302 320,324 540,316 L540,336 L0,336 Z" fill="#fff"/>
      <path d="M0,284 C150,314 330,332 540,325 L540,336 L0,336 Z" fill="url(#blueA)"/>
    </svg>
    <div class="brand">
      <div class="brand-row"><span class="brand-dot"></span><span class="brand-name">VORK</span></div>
      <div class="brand-tagline">BRIDGING HORIZONS</div>
    </div>
    <div class="contact">
      <div class="person-name">Rajesh Motla</div>
      <div class="person-title">Managing Director</div>
      <div class="address">B.P. No.6213, Commune-3,<br>Near Toravi Laundry,<br>Kaleba Zone,<br>Bamako-Mali</div>
      <div class="contact-row"><svg viewBox="0 0 10 10"><path d="M2 1h2l1 2-1 1a5 5 0 0 0 2 2l1-1 2 1v2a1 1 0 0 1-1 1A8 8 0 0 1 1 2a1 1 0 0 1 1-1z" fill="var(--brand-blue)"/></svg>+223-20418836</div>
      <div class="contact-row"><svg viewBox="0 0 10 10"><rect x="3" y="1" width="4" height="8" rx="1" fill="var(--brand-blue)"/></svg>+223-76249031</div>
      <div class="contact-row"><svg viewBox="0 0 10 10"><circle cx="5" cy="5" r="5" fill="var(--brand-blue)"/><rect x="2.5" y="3.5" width="5" height="3.5" fill="#fff"/></svg>rajesh@vork.co.in</div>
      <div class="contact-row"><svg viewBox="0 0 10 10"><circle cx="5" cy="5" r="4.2" fill="none" stroke="var(--brand-blue)" stroke-width="1.2"/><path d="M1 5h8M5 1v8" stroke="var(--brand-blue)" stroke-width=".8"/></svg>www.vork.co.in</div>
    </div>
  </section>
  <div class="option-label label-front-a">Business Card Front Option A</div>

  <!-- Front option B -->
  <section class="card front-b">
    <svg class="swoosh" viewBox="0 0 540 336" aria-hidden="true">
      <defs>
        <linearGradient id="greenB" x1="0" x2="1"><stop offset="0" stop-color="var(--green)"/><stop offset="1" stop-color="var(--green-light)"/></linearGradient>
        <linearGradient id="blueB" x1="0" x2="1"><stop offset="0" stop-color="var(--blue-light)"/><stop offset="1" stop-color="var(--brand-blue)"/></linearGradient>
      </defs>
      <path d="M0,300 C150,292 360,270 540,232 L540,336 L0,336 Z" fill="url(#greenB)"/>
      <path d="M0,312 C170,306 370,290 540,262 L540,336 L0,336 Z" fill="#fff"/>
      <path d="M0,322 C180,318 380,304 540,282 L540,336 L0,336 Z" fill="url(#blueB)"/>
    </svg>
    <div class="brand">
      <div class="brand-row"><span class="brand-dot"></span><span class="brand-name">VORK</span></div>
      <div class="brand-tagline">BRIDGING HORIZONS</div>
    </div>
    <div class="contact">
      <div class="person-name">Rajesh Motla</div>
      <div class="person-title">Managing Director</div>
      <div class="contact-row address"><svg viewBox="0 0 10 10"><path d="M5 0a3.5 3.5 0 0 1 3.5 3.5C8.5 6 5 10 5 10S1.5 6 1.5 3.5A3.5 3.5 0 0 1 5 0z" fill="var(--brand-blue)"/></svg><span>B.P. No.6213, Commune-3,<br>Near Toravi Laundry, Kaleba Zone,<br>Bamako-Mali</span></div>
      <div class="contact-row"><svg viewBox="0 0 10 10"><path d="M2 1h2l1 2-1 1a5 5 0 0 0 2 2l1-1 2 1v2a1 1 0 0 1-1 1A8 8 0 0 1 1 2a1 1 0 0 1 1-1z" fill="var(--brand-blue)"/></svg>+223-20418836</div>
      <div class="contact-row"><svg viewBox="0 0 10 10"><rect x="3" y="1" width="4" height="8" rx="1" fill="var(--brand-blue)"/></svg>+223-76249031</div>
      <div class="contact-row"><svg viewBox="0 0 10 10"><circle cx="5" cy="5" r="5" fill="var(--brand-blue)"/><rect x="2.5" y="3.5" width="5" height="3.5" fill="#fff"/></svg>rajesh@vork.co.in</div>
      <div class="contact-row"><svg viewBox="0 0 10 10"><circle cx="5" cy="5" r="4.2" fill="none" stroke="var(--brand-blue)" stroke-width="1.2"/><path d="M1 5h8M5 1v8" stroke="var(--brand-blue)" stroke-width=".8"/></svg>www.vork.co.in</div>
    </div>
  </section>
  <div class="option-label label-front-b">Business Card Front Option B</div>

  <!-- Back option A -->
  <section class="card back-a">
    <div class="brand">
      <div class="brand-row"><span class="brand-dot"></span><span class="brand-name">VORK</span></div>
      <div class="brand-tagline">BRIDGING HORIZONS</div>
    </div>
    <div class="office">
      <div class="office-title">India Office</div>
      <div class="office-address"><span><svg viewBox="0 0 10 10"><path d="M5 1 1 5h1.5v4h5V5H9z" fill="var(--brand-blue)"/></svg>D-47, Palm Enclave-II, Gurgaon, Haryana 122015</span></div>
      <div class="office-phones">
        <span><svg viewBox="0 0 10 10"><path d="M2 1h2l1 2-1 1a5 5 0 0 0 2 2l1-1 2 1v2a1 1 0 0 1-1 1A8 8 0 0 1 1 2a1 1 0 0 1 1-1z" fill="var(--brand-blue)"/></svg>+91-124-4708352</span>
        <span><svg viewBox="0 0 10 10"><rect x="1" y="3" width="8" height="6" fill="var(--brand-blue)"/><rect x="3" y="1" width="4" height="3" fill="var(--brand-blue)"/></svg>+91-124-4519267</span>
        <span><svg viewBox="0 0 10 10"><rect x="3" y="1" width="4" height="8" rx="1" fill="var(--brand-blue)"/></svg>+91-9871436029</span>
      </div>
    </div>
  </section>
  <div class="option-label label-back-a">Business Card Back Option A</div>

  <!-- Back option B -->
  <section class="card back-b">
    <div class="brand">
      <div class="brand-row"><span class="brand-dot"></span><span class="brand-name">VORK</span></div>
    </div>
    <div class="office">
      <div class="office-title">India Office</div>
      <div class="office-address"><span><svg viewBox="0 0 10 10"><path d="M5 1 1 5h1.5v4h5V5H9z" fill="var(--brand-blue)"/></svg>D-47, Palm Enclave-II, Gurgaon, Haryana 122015</span></div>
      <div class="office-phones">
        <span><svg viewBox="0 0 10 10"><path d="M2 1h2l1 2-1 1a5 5 0 0 0 2 2l1-1 2 1v2a1 1 0 0 1-1 1A8 8 0 0 1 1 2a1 1 0 0 1 1-1z" fill="var(--brand-blue)"/></svg>+91-124-4708352</span>
        <span><svg viewBox="0 0 10 10"><rect x="1" y="3" width="8" height="6" fill="var(--brand-blue)"/><rect x="3" y="1" width="4" height="3" fill="var(--brand-blue)"/></svg>+91-124-4519267</span>
        <span><svg viewBox="0 0 10 10"><rect x="3" y="1" width="4" height="8" rx="1" fill="var(--brand-blue)"/></svg>+91-9871436029</span>
      </div>
    </div>
  </section>
  <div class="option-label label-back-b">Business Card Back Option B</div>

</body>
</html>
```